Brisk Tide Womens Shaving Foam (For sale in supermarkets).

We supply supermarkets with various products and now need a new design for a Ladies Shaving Foam Can. Soft Pink on the bottom of the can finishing of gradated into white. Needs to have a Shaving Foam swirl image also needs to have our Brisk Tide Logo. White base Can with mainly soft pink. I have mocked one up with Brisk Tide Logo in the middle similar to the Body Spray cans. Good Luck.
Target Market(s)
Females
Industry/Entity Type
Grocery
Colors
ffffff
e34197
e667a6
eea4c8
f9d9e8
Requirements
Must have
- White Can base with Pink colour tones
Nice to have
- Modern fresh feel
Should not have
- No dark colours soft pinks

```html
<!DOCTYPE html>
<html lang="en">
<head>
<meta charset="utf-8">
<title>Brisk Tide Sensitive Shaving Foam</title>
<link rel="stylesheet" href="https://fonts.googleapis.com/css2?family=Lobster+Two:ital,wght@0,700;1,700&display=swap">
<style>
  :root {
    --white: #ffffff;
    --pink-deep: #e34197;
    --pink-strong: #e667a6;
    --pink-mid: #eea4c8;
    --pink-soft: #f9d9e8;
    --cap-pink: #f6bdc6;
    --cap-shade: #d99aa5;
    --logo-pink: #ef8fb4;
    --stage: #f1f1f1;
    --rule: #d8d8d8;
  }
  html, body {
    margin: 0;
    padding: 0;
    width: 1136px;
    height: 1200px;
    overflow: hidden;
    background: var(--stage);
  }
  .canvas {
    position: relative;
    width: 1136px;
    height: 1200px;
  }
  .can {
    position: absolute;
    left: 428px;
    top: 55px;
    width: 280px;
    height: 1090px;
    border-radius: 4px 4px 10px 10px;
    overflow: hidden;
    background: linear-gradient(to bottom,
      var(--white) 0%,
      var(--white) 52%,
      var(--pink-soft) 72%,
      #f6c2d4 88%,
      #f3adc6 100%);
  }
  .can__cap {
    position: absolute;
    left: 0; top: 0;
    width: 100%;
    height: 236px;
    background: var(--cap-pink);
    border-bottom: 2px solid var(--cap-shade);
    border-radius: 4px 4px 0 0;
  }
  .can__collar-rule {
    position: absolute;
    left: 0; top: 283px;
    width: 100%;
    height: 2px;
    background: var(--rule);
  }
  .brand {
    position: absolute;
    left: 46px;
    top: 392px;
    width: 100px;
    height: 420px;
  }
  .brand__name {
    position: absolute;
    left: 50%;
    top: 50%;
    width: 420px;
    transform: translate(-50%, -50%) rotate(-90deg);
    text-align: center;
    font-family: "Lobster Two", cursive;
    font-weight: 700;
    font-style: normal;
    font-size: 84px;
    line-height: 1;
    color: var(--logo-pink);
    white-space: nowrap;
  }
  .variant-band {
    position: absolute;
    left: 184px;
    top: 391px;
    width: 42px;
    height: 421px;
    background: var(--logo-pink);
  }
  .variant-band__text {
    position: absolute;
    left: 50%;
    top: 120px;
    width: 220px;
    transform: translate(-50%, -50%) rotate(-90deg);
    text-align: center;
    font-family: "Lobster Two", cursive;
    font-style: italic;
    font-weight: 700;
    font-size: 31px;
    line-height: 1;
    color: var(--white);
    white-space: nowrap;
  }
  .foam-swirl {
    position: absolute;
    left: 87px;
    top: 852px;
    width: 106px;
    height: 96px;
  }
  .product-type {
    position: absolute;
    left: 0;
    top: 960px;
    width: 100%;
    text-align: center;
    font-family: "Lobster Two", cursive;
    font-style: italic;
    font-weight: 700;
    font-size: 31px;
    line-height: 1;
    color: var(--pink-strong);
  }
  .product-name {
    position: absolute;
    left: 16px;
    top: 1003px;
    width: 248px;
    height: 40px;
    background: var(--pink-strong);
    transform: skewX(-6deg);
  }
  .product-name__text {
    display: block;
    transform: skewX(6deg);
    text-align: center;
    font-family: "Lobster Two", cursive;
    font-style: italic;
    font-weight: 700;
    font-size: 30px;
    line-height: 40px;
    color: var(--white);
    white-space: nowrap;
  }
  .volume {
    position: absolute;
    left: 0;
    top: 1050px;
    width: 100%;
    text-align: center;
    font-family: "Lobster Two", cursive;
    font-style: italic;
    font-weight: 700;
    font-size: 22px;
    line-height: 1;
    color: var(--pink-strong);
  }
</style>
</head>
<body>
<main class="canvas">
  <div class="can">
    <div class="can__cap"></div>
    <div class="can__collar-rule"></div>

    <div class="brand">
      <span class="brand__name">Brisk Tide</span>
    </div>

    <div class="variant-band">
      <span class="variant-band__text">soft bloom</span>
    </div>

    <svg class="foam-swirl" viewBox="0 0 106 96" role="img" aria-label="Swirl of white shaving foam">
      <defs>
        <radialGradient id="foamTone" cx="45%" cy="35%" r="70%">
          <stop offset="0%" stop-color="#ffffff"/>
          <stop offset="75%" stop-color="#f4f4f4"/>
          <stop offset="100%" stop-color="#e2e2e2"/>
        </radialGradient>
      </defs>
      <ellipse cx="53" cy="88" rx="44" ry="6" fill="#f3a9c4" opacity="0.6"/>
      <ellipse cx="53" cy="58" rx="52" ry="32" fill="url(#foamTone)"/>
    </svg>

    <div class="product-type">Sensitive</div>
    <div class="product-name"><span class="product-name__text">Shaving Foam</span></div>
    <div class="volume">200ml</div>
  </div>
</main>
</body>
</html>
```